PDN Letterhead

We need a letterhead design that will be able to be used on all marketing products (letterhead, mail chimp, envelops, business cards, etc.) We are a law firm specializing primarily in transportation law but offer a wide range of services to our clients. We would like the design to be modern, simple, and professional. Our colors are black and gold, however, we've incorporated dark gray and white on other marketing products such as our website.

```html
<!DOCTYPE html>
<html lang="en">
<head>
<meta charset="utf-8">
<title>PDN Law Group – Stationery</title>
<link rel="stylesheet" href="https://fonts.googleapis.com/css2?family=Open+Sans:ital,wght@0,400;0,600;1,400&display=swap">
<style>
  :root {
    --bg-top: #2b2a2a;
    --bg-bottom: #211f1f;
    --gold: #b89c72;
    --gold-dark: #a68b66;
    --window-grey: #e4e4e2;
    --paper: #ffffff;
    --ink: #111111;
    --navy: #1c2340;
    --shadow: 6px 6px 10px rgba(0,0,0,0.55);
  }
  html, body {
    margin: 0;
    padding: 0;
    width: 1200px;
    height: 1200px;
    overflow: hidden;
  }
  body {
    background: linear-gradient(180deg, var(--bg-top), var(--bg-bottom));
    font-family: "Open Sans", Arial, sans-serif;
    color: var(--ink);
  }
  .stage {
    position: absolute;
    left: 0;
    top: 0;
    width: 1932px;
    height: 1932px;
    transform: scale(0.621118);
    transform-origin: 0 0;
  }
  .sheet {
    position: absolute;
    overflow: hidden;
    box-shadow: var(--shadow);
    background: var(--paper);
  }
  .sheet > svg.art {
    position: absolute;
    left: 0;
    top: 0;
    width: 100%;
    height: 100%;
  }
  .wordmark {
    position: absolute;
    text-align: center;
    color: var(--ink);
    line-height: 1;
    transform: translateX(-50%);
    white-space: nowrap;
  }
  .wordmark .name { display: block; font-weight: 600; letter-spacing: 0.04em; }
  .wordmark .sub { display: block; font-weight: 400; letter-spacing: 0.18em; margin-top: 0.25em; }

  /* Business card – front */
  .card-front { left: 83px; top: 507px; width: 283px; height: 170px; background: var(--gold); }
  .card-front .wordmark { left: 86px; top: 80px; }
  .card-front .name { font-size: 28px; }
  .card-front .sub { font-size: 13px; }

  /* Business card – back */
  .card-back { left: 83px; top: 718px; width: 283px; height: 169px; }
  .card-back .person { position: absolute; left: 33px; top: 48px; color: var(--navy); }
  .card-back .person-name { font-size: 18px; line-height: 1.2; font-weight: 600; }
  .card-back .person-role { font-size: 11px; font-style: italic; line-height: 1.3; }
  .card-back .contact { position: absolute; top: 117px; font-size: 8.5px; line-height: 14px; color: var(--navy); }
  .card-back .contact.left { left: 33px; }
  .card-back .contact.right { left: 147px; }

  /* Envelope – front */
  .envelope-front { left: 397px; top: 507px; width: 706px; height: 330px; }
  .envelope-front .wordmark { left: 143px; top: 160px; }
  .envelope-front .name { font-size: 44px; }
  .envelope-front .sub { font-size: 19px; }

  /* Envelope – back */
  .envelope-back { left: 397px; top: 934px; width: 706px; height: 329px; }
  .envelope-back .web {
    position: absolute; left: 0; right: 0; top: 46px;
    text-align: center; font-size: 17px; letter-spacing: 0.22em; color: var(--ink);
  }
  .contact-line {
    position: absolute; left: 0; right: 0;
    display: flex; justify-content: center; align-items: center;
    font-size: 11px; color: var(--ink);
  }
  .contact-line .sep { width: 2px; height: 22px; margin: 0 22px; }
  .envelope-back .contact-line { top: 262px; }
  .envelope-back .sep { background: var(--gold); }

  /* Letterhead */
  .letterhead { left: 1189px; top: 507px; width: 660px; height: 918px; }
  .letterhead .wordmark { left: 330px; top: 88px; }
  .letterhead .name { font-size: 40px; }
  .letterhead .sub { font-size: 19px; color: var(--gold); }
  .letterhead .footer {
    position: absolute; left: 0; right: 0; bottom: 0; height: 44px;
    background: var(--gold-dark);
  }
  .letterhead .contact-line { top: 11px; }
  .letterhead .sep { background: var(--paper); }
</style>
</head>
<body>
<main class="stage">

  <section class="sheet card-front" aria-label="Business card front">
    <div class="wordmark"><span class="name">PDN</span><span class="sub">LAW GROUP</span></div>
  </section>

  <section class="sheet card-back" aria-label="Business card back">
    <div class="person">
      <div class="person-name">Lorem Ipsum</div>
      <div class="person-role">Director</div>
    </div>
    <div class="contact left">12.st city country 12345<br>+12 3456 7890</div>
    <div class="contact right">info@pdnlawgroup.com<br>www.pdnlawgroup.com</div>
  </section>

  <section class="sheet envelope-front" aria-label="Envelope front">
    <svg class="art" viewBox="0 0 706 330" aria-hidden="true">
      <rect class="brand-panel" x="0" y="0" width="284" height="330" fill="var(--gold)"/>
      <rect class="window" x="426" y="151" width="209" height="87" rx="8" fill="var(--window-grey)"/>
    </svg>
    <div class="wordmark"><span class="name">PDN</span><span class="sub">LAW GROUP</span></div>
  </section>

  <section class="sheet envelope-back" aria-label="Envelope back">
    <svg class="art" viewBox="0 0 706 329" aria-hidden="true">
      <path class="flap" d="M0,0 H706 L662,94 Q651,111 630,111 H72 Q53,111 43,94 Z" fill="var(--gold)"/>
    </svg>
    <div class="web">www.pdnlawgroup.com</div>
    <div class="contact-line">
      <span>12.st city country 12345</span><span class="sep"></span>
      <span>+12 3456 7890</span><span class="sep"></span>
      <span>info@pdnlawgroup.com</span>
    </div>
  </section>

  <section class="sheet letterhead" aria-label="Letterhead">
    <div class="wordmark"><span class="name">PDN</span><span class="sub">LAW GROUP</span></div>
    <footer class="footer">
      <div class="contact-line">
        <span>12.st city country 12345</span><span class="sep"></span>
        <span>+12 3456 7890</span><span class="sep"></span>
        <span>info@pdnlawgroup.com</span>
      </div>
    </footer>
  </section>

</main>
</body>
</html>
```